Vehicle Design

I would like the Van done with the logo and things that we do it need to look professional,
The link it to a car site for a 2003 VH Orvane Kestrel this is the same as i have so hope you can use the photos of here, or get the specs that you need, I have a sign person that does all my vehicles, so will need to pass the winning file to him,
Target Market(s)
mobile advertising police and housing
Industry/Entity Type
It Professional
Requirements
Must have
- logo, phone number 0468 357 921 what we do link attached,was hopping to have emblem on doors at rear, and sides done with style
Should be discrete but still make a noise
Nice to have
- Smoke that is in card that is attached
Should not have
- should not be too much not to scare clients from having me outside,

```html
<!DOCTYPE html>
<html lang="en">
<head>
<meta charset="utf-8">
<title>Orvane Kestrel Van Livery – Kessa Response Cleanup Specialists</title>
<link rel="stylesheet" href="https://fonts.googleapis.com/css2?family=Anton&family=Roboto+Condensed:wght@700&display=swap">
<style>
  :root {
    --wrap-yellow: #f7d417;
    --wrap-yellow-deep: #e8c20c;
    --ink: #111111;
    --trim-grey: #a9abae;
    --glass-grey: #cfd1d3;
    --tyre: #1d1d1d;
    --hub: #d9d9d9;
    --tail-red: #c8202a;
    --page: #ffffff;
  }
  html, body {
    margin: 0;
    width: 1200px;
    height: 752px;
    overflow: hidden;
    background: var(--page);
  }
  .livery-sheet { display: block; width: 1200px; height: 752px; }

  .body-panel { fill: var(--wrap-yellow); stroke: var(--ink); stroke-width: 1; }
  .trim { fill: var(--trim-grey); stroke: #6f7173; stroke-width: 0.8; }
  .glass { fill: var(--glass-grey); stroke: #6f7173; stroke-width: 0.8; }
  .tyre { fill: var(--tyre); }
  .hub { fill: var(--hub); stroke: #777; stroke-width: 1; }
  .tail-light { fill: var(--tail-red); }
  .panel-line { fill: none; stroke: #8a7a10; stroke-width: 0.8; }
  .rear-window { fill: var(--wrap-yellow-deep); stroke: #8a7a10; stroke-width: 0.8; }

  .headline {
    font-family: "Anton", "Impact", sans-serif;
    fill: var(--wrap-yellow);
    stroke: var(--ink);
    stroke-width: 1.3;
    paint-order: stroke;
    letter-spacing: 0.3px;
  }
  .phone {
    font-family: "Anton", "Impact", sans-serif;
    fill: var(--wrap-yellow);
    stroke: var(--ink);
    stroke-width: 1.4;
    paint-order: stroke;
    letter-spacing: 1px;
  }
  .service-list, .tagline, .brand-name {
    font-family: "Roboto Condensed", "Arial Narrow", sans-serif;
    font-weight: 700;
    fill: var(--ink);
  }
  .brand-dot { fill: none; stroke: var(--ink); stroke-width: 1.6; }
  .make-badge {
    font-family: "Roboto Condensed", "Arial Narrow", sans-serif;
    font-weight: 700;
    fill: #555;
  }
  .map-emblem-area { fill: rgba(17,17,17,0.12); }
</style>
</head>
<body>
<svg class="livery-sheet" viewBox="0 0 1200 752" xmlns="http://www.w3.org/2000/svg">
  <defs>
    <linearGradient id="smokeRight" x1="0" y1="0" x2="1" y2="0">
      <stop offset="0" stop-color="#6b6b55" stop-opacity="0"/>
      <stop offset="1" stop-color="#5a5a48" stop-opacity="0.3"/>
    </linearGradient>
    <linearGradient id="smokeLeft" x1="1" y1="0" x2="0" y2="0">
      <stop offset="0" stop-color="#6b6b55" stop-opacity="0"/>
      <stop offset="1" stop-color="#5a5a48" stop-opacity="0.3"/>
    </linearGradient>
  </defs>

  <!-- Front view -->
  <g class="van-front">
    <rect class="trim" x="6" y="86" width="18" height="24" rx="3"/>
    <rect class="trim" x="211" y="86" width="18" height="24" rx="3"/>
    <path class="body-panel" d="M32 170 L30 60 Q34 8 70 4 L165 4 Q201 8 205 60 L203 170 Z"/>
    <path class="glass" d="M44 94 L50 40 Q54 32 64 32 L171 32 Q181 32 185 40 L191 94 Z"/>
    <g class="brand-lockup">
      <circle class="brand-dot" cx="94" cy="16" r="8"/>
      <text class="brand-name" x="106" y="20" font-size="11">Kessa Response</text>
    </g>
    <text class="phone" x="117.5" y="124" font-size="18" text-anchor="middle">0468 357 921</text>
    <rect class="trim" x="36" y="134" width="34" height="14" rx="4"/>
    <rect class="trim" x="165" y="134" width="34" height="14" rx="4"/>
    <rect class="trim" x="76" y="138" width="83" height="12" rx="3"/>
    <text class="make-badge" x="117.5" y="147" font-size="7" text-anchor="middle">ORVANE</text>
    <rect class="trim" x="26" y="158" width="183" height="26" rx="6"/>
    <rect x="89" y="163" width="57" height="14" fill="var(--wrap-yellow)" stroke="#6f7173" stroke-width="0.8"/>
    <rect class="tyre" x="30" y="184" width="22" height="40" rx="4"/>
    <rect class="tyre" x="183" y="184" width="22" height="40" rx="4"/>
  </g>

  <!-- Rear view -->
  <g class="van-rear">
    <rect class="trim" x="259" y="86" width="18" height="24" rx="3"/>
    <rect class="trim" x="473" y="86" width="18" height="24" rx="3"/>
    <path class="body-panel" d="M283 182 L281 30 Q283 4 310 2 L440 2 Q467 4 469 30 L467 182 Z"/>
    <rect class="tail-light" x="282" y="114" width="16" height="42"/>
    <rect class="tail-light" x="452" y="114" width="16" height="42"/>
    <line class="panel-line" x1="375" y1="8" x2="375" y2="178"/>
    <rect class="rear-window" x="312" y="44" width="126" height="64" rx="3"/>
    <text class="headline" x="375" y="20" font-size="14" text-anchor="middle">Kessa Response</text>
    <text class="headline" x="375" y="37" font-size="14" text-anchor="middle">Cleanup Specialists</text>
    <text class="service-list" text-anchor="middle">
      <tspan x="375" y="52" font-size="7.5">Crime and Trauma Scene</tspan>
      <tspan x="375" y="61" font-size="7.5">Cleanup &amp; Decontamination</tspan>
      <tspan x="375" y="70" font-size="5.6">Mould Inspections &amp; Remedies</tspan>
      <tspan x="375" y="78" font-size="5.6">Drug lab Decontamination and Hoddie cleanups</tspan>
      <tspan x="375" y="86" font-size="5.6">Odour control</tspan>
      <tspan x="375" y="94" font-size="5.6">Air Quality Testing and swabs</tspan>
      <tspan x="375" y="102" font-size="5.6">Hydoxyl Machine, Ozone Machine, Sterilizing Light</tspan>
      <tspan x="375" y="118" font-size="6">Commercial Steam machines</tspan>
      <tspan x="375" y="127" font-size="6">Thermal Imaging, Bacteria Testing</tspan>
    </text>
    <text class="phone" x="337" y="166" font-size="13" text-anchor="middle">0468 357 921</text>
    <g class="brand-lockup">
      <circle class="brand-dot" cx="400" cy="146" r="6"/>
      <text class="brand-name" x="409" y="144" font-size="8">Kessa</text>
      <text class="brand-name" x="409" y="153" font-size="8">Response</text>
    </g>
    <rect class="trim" x="280" y="178" width="190" height="16" rx="4"/>
    <rect class="tyre" x="286" y="194" width="20" height="30" rx="4"/>
    <rect class="tyre" x="444" y="194" width="20" height="30" rx="4"/>
  </g>

  <!-- Side view, cab on the left -->
  <g class="van-side-left">
    <path class="body-panel" d="M4 442 L6 410 Q10 396 30 392 L88 372 L150 294 Q162 278 190 277 L520 274 Q538 276 538 296 L538 456 L4 456 Z"/>
    <path class="glass" d="M96 366 L146 304 Q150 300 156 300 L186 300 L186 366 Z"/>
    <rect class="trim" x="88" y="350" width="8" height="16" rx="2"/>
    <line class="panel-line" x1="194" y1="286" x2="194" y2="436"/>
    <line class="panel-line" x1="392" y1="280" x2="392" y2="436"/>
    <rect x="470" y="282" width="66" height="140" fill="url(#smokeRight)" role="img" aria-label="Drifting grey smoke wisps"/>
    <rect class="map-emblem-area" x="206" y="284" width="150" height="146" rx="30" role="img" aria-label="Map of Australia outline with large biohazard emblem"/>
    <text class="headline" x="358" y="306" font-size="24" text-anchor="middle">Kessa Response</text>
    <text class="headline" x="358" y="333" font-size="24" text-anchor="middle">Cleanup Specialists</text>
    <text class="service-list" font-size="7.2">
      <tspan x="370" y="348">Mould Inspections &amp; Remedies</tspan>
      <tspan x="370" y="357">Drug lab Decontamination and Hoddie cleanups</tspan>
      <tspan x="370" y="366">Odour control</tspan>
      <tspan x="370" y="375">Air Quality Testing and swabs</tspan>
      <tspan x="370" y="386">Hydoxyl Machine, Ozone Machine, Sterilizing Light</tspan>
      <tspan x="370" y="395">Commercial Steam machines</tspan>
      <tspan x="370" y="404">Thermal Imaging, Bacteria Testing</tspan>
    </text>
    <g class="brand-lockup">
      <circle class="brand-dot" cx="122" cy="404" r="8"/>
      <text class="brand-name" x="134" y="401" font-size="10">Kessa</text>
      <text class="brand-name" x="134" y="412" font-size="10">Response</text>
    </g>
    <text class="phone" x="284" y="432" font-size="27" text-anchor="middle">0468 357 921</text>
    <rect class="trim" x="2" y="436" width="538" height="22"/>
    <text class="tagline" x="270" y="452" font-size="10" text-anchor="middle">Crime and trauma scene cleanup &amp; Decontamination</text>
    <circle class="tyre" cx="98" cy="466" r="34"/>
    <circle class="hub" cx="98" cy="466" r="16"/>
    <circle class="tyre" cx="444" cy="466" r="34"/>
    <circle class="hub" cx="444" cy="466" r="16"/>
  </g>

  <!-- Side view, cab on the right -->
  <g class="van-side-right">
    <path class="body-panel" d="M2 706 L2 550 Q2 530 22 529 L350 527 Q378 528 392 544 L452 622 L510 642 Q530 646 534 660 L536 706 Z"/>
    <path class="glass" d="M352 546 L382 546 Q388 546 392 552 L442 618 L352 618 Z"/>
    <rect class="trim" x="440" y="604" width="8" height="16" rx="2"/>
    <line class="panel-line" x1="344" y1="534" x2="344" y2="690"/>
    <line class="panel-line" x1="150" y1="534" x2="150" y2="690"/>
    <rect x="4" y="536" width="50" height="140" fill="url(#smokeLeft)" role="img" aria-label="Drifting grey smoke wisps"/>
    <rect class="map-emblem-area" x="196" y="536" width="144" height="146" rx="30" role="img" aria-label="Map of Australia outline with large biohazard emblem"/>
    <text class="headline" x="188" y="558" font-size="24" text-anchor="middle">Kessa Response</text>
    <text class="headline" x="188" y="585" font-size="24" text-anchor="middle">Cleanup Specialists</text>
    <text class="service-list" font-size="7.2" text-anchor="middle">
      <tspan x="112" y="598">Mould Inspections &amp; Remedies</tspan>
      <tspan x="112" y="607">Odour control</tspan>
      <tspan x="112" y="616">Drug lab Decontamination and Hoddie cleanups</tspan>
      <tspan x="112" y="625">Hydoxyl Machine, Ozone Machine, Sterilizing Light</tspan>
      <tspan x="140" y="640">Air Quality Testing and swabs</tspan>
      <tspan x="140" y="649">Commercial Steam machines</tspan>
      <tspan x="140" y="658">Thermal Imaging, Bacteria Testing</tspan>
    </text>
    <g class="brand-lockup">
      <circle class="brand-dot" cx="414" cy="662" r="8"/>
      <text class="brand-name" x="426" y="659" font-size="10">Kessa</text>
      <text class="brand-name" x="426" y="670" font-size="10">Response</text>
    </g>
    <text class="phone" x="258" y="688" font-size="27" text-anchor="middle">0468 357 921</text>
    <rect class="trim" x="0" y="692" width="540" height="22"/>
    <text class="tagline" x="272" y="708" font-size="10" text-anchor="middle">Crime and trauma scene cleanup &amp; Decontamination</text>
    <circle class="tyre" cx="98" cy="716" r="34"/>
    <circle class="hub" cx="98" cy="716" r="16"/>
    <circle class="tyre" cx="444" cy="716" r="34"/>
    <circle class="hub" cx="444" cy="716" r="16"/>
  </g>
</svg>
</body>
</html>
```